US company marketing to law enforcement needs brochure design

We have created a new logo and now need to update our printed material. What we really need is a "style" or "template" for how our brochures will look in the future. Enclosed is the brochure draft with the old style and logo. Also enclosed is the new logo. As we are marketing to US law enforcement it is important the the brochure design is strong, powerful and that we are looking experienced and trustworthy. However, we also want to look modern in line with the logo update.

Target Market(s)

Law enforcement

Industry/Entity Type

Marketing

```html
<!DOCTYPE html>
<html lang="en">
<head>
<meta charset="utf-8">
<title>Meridian Justice – Offender Programs Brochure</title>
<link rel="stylesheet" href="https://fonts.googleapis.com/css2?family=Open+Sans:wght@400;600;700&family=Roboto+Condensed:wght@700&family=Marcellus+SC&display=swap">
<style>
  :root{
    --navy:#233a70;
    --navy-deep:#1d3163;
    --steel:#9aa3b8;
    --mist:#ebebeb;
    --silver:#d3d6db;
    --slate:#8f8f8f;
    --stone:#e6e3df;
    --white:#ffffff;
    --ink:#3d4a66;
  }
  *{box-sizing:border-box;margin:0;padding:0}
  html,body{width:922px;height:1200px;overflow:hidden}
  body{background:var(--stone);font-family:"Open Sans",Arial,sans-serif;position:relative}

  .spread{position:absolute;left:67px;width:762px;height:496px;box-shadow:0 2px 8px rgba(0,0,0,.18);background:var(--white)}
  .spread--outer{top:90px}
  .spread--inner{top:610px}
  .panel{position:absolute;top:0;width:381px;height:100%;overflow:hidden}
  .panel--left{left:0}
  .panel--right{left:381px;border-left:1px solid rgba(0,0,0,.12)}

  .band{position:absolute;left:0;width:100%}
  .band--navy{background:var(--navy)}
  .band--mist{background:var(--mist)}
  .band--silver{background:var(--silver)}
  .band--slate{background:var(--slate)}

  .photo{position:absolute}
  .photo--handshake{background:linear-gradient(120deg,#dfe6ee 0%,#b9c6d6 40%,#e4c2a6 55%,#a9b7c9 75%,#eef2f6 100%)}
  .photo--courthouse{background:linear-gradient(90deg,#8a6a2e 0%,#b68e45 22%,#d9dde0 38%,#c4c9cc 70%,#e8ebec 100%)}
  .photo--meeting{background:linear-gradient(110deg,#d9e2ea 0%,#c9a98c 35%,#b07f62 55%,#6d7078 80%,#c7ced6 100%)}

  .brand{position:absolute;left:0;width:100%;display:flex;align-items:center;justify-content:center;gap:10px}
  .brand__mark{width:38px;height:38px;border-radius:50%;background:var(--navy)}
  .brand__name{font-family:"Open Sans",Arial,sans-serif;font-weight:400;font-size:21px;color:#8a8d93}

  .cond-title{font-family:"Roboto Condensed",Arial,sans-serif;font-weight:700;text-transform:uppercase}
  .caps{font-family:"Marcellus SC",Georgia,serif}

  .cover-title{top:24px;text-align:center;font-size:19px;color:var(--steel);letter-spacing:.3px}
  .contact{text-align:center;color:var(--white)}
  .contact__web{font-size:14px;letter-spacing:1.4px}
  .contact__phone{font-size:14px;margin-top:8px;letter-spacing:.5px}
  .cover-sub{text-align:center;color:var(--white)}
  .cover-sub__title{font-family:"Roboto Condensed",Arial,sans-serif;font-weight:700;font-size:19px}
  .cover-sub__stages{font-size:10px;color:#d7ddea;line-height:13px;margin-top:6px;letter-spacing:.4px}

  .intro{text-align:center;color:var(--white)}
  .intro__title{font-size:19px;margin-top:22px}
  .intro__lead{font-size:12.5px;line-height:17px;margin-top:8px;color:#e5e9f2}

  .stages{position:absolute;left:14px;top:110px}

  .pitch{text-align:center}
  .pitch__head{color:var(--navy);font-size:20px;font-weight:700;margin-top:20px;line-height:24px}
  .pitch__head span{display:block;font-weight:400;font-size:19px}
  .pitch__body{margin-top:22px;font-size:10px;line-height:14px;color:#333;letter-spacing:.4px;text-transform:uppercase}

  .custom{text-align:center;color:var(--white);padding-top:4px}
  .custom__title{font-size:14px;letter-spacing:.6px}
  .custom__note{font-size:7.5px;margin-top:2px}

  .menus{position:absolute;top:190px;left:20px;right:10px;display:flex;gap:18px}
  .menu__title{color:var(--navy);font-size:10.5px;line-height:12px;margin-bottom:6px}
  .menu__cols{display:flex;gap:16px}
  .menu ul{list-style:none}
  .menu li{font-size:5.8px;line-height:9.6px;color:#444;display:flex;align-items:center;gap:4px}
  .menu li::before{content:"";width:5px;height:4px;background:var(--navy);flex:none}
  .menu--full{width:205px}
  .menu--admin{flex:1}

  .strip{display:flex;align-items:center;justify-content:center;color:var(--white);height:24px}
  .strip--phone{font-size:12.5px;letter-spacing:.6px}
  .strip--web{font-size:12.5px;letter-spacing:1.4px}

  .features{position:absolute;top:335px;left:0;width:100%;height:161px;display:flex}
  .feature{flex:1;padding:14px 16px 0 20px;color:var(--white);border-right:1px solid rgba(255,255,255,.12)}
  .feature:last-child{border-right:none}
  .feature__title{font-size:10.5px;line-height:12px;margin-bottom:14px;letter-spacing:.3px}
  .feature p{font-size:5.2px;line-height:9px;color:#dfe4ef;text-align:justify;margin-bottom:8px}
</style>
</head>
<body>

<section class="spread spread--outer" aria-label="Outer spread">
  <div class="panel panel--left">
    <div class="band band--navy" style="top:0;height:76px"></div>
    <div class="band band--mist" style="top:76px;height:77px">
      <div class="brand" style="top:19px"><span class="brand__mark"></span><span class="brand__name">Meridian Justice</span></div>
    </div>
    <div class="photo photo--handshake" style="left:0;top:153px;width:381px;height:268px" role="img" aria-label="Photo of two business people shaking hands"></div>
    <div class="band band--navy contact" style="top:421px;height:75px;padding-top:16px">
      <div class="contact__web">www.meridianjustice.org</div>
      <div class="contact__phone">1-800-555-0142</div>
    </div>
  </div>

  <div class="panel panel--right">
    <div class="band band--navy" style="top:0;height:76px">
      <div class="band cond-title cover-title">Comprehensive Offender Solution</div>
    </div>
    <div class="band band--mist" style="top:76px;height:77px">
      <div class="brand" style="top:19px"><span class="brand__mark"></span><span class="brand__name">Meridian Justice</span></div>
    </div>
    <div class="photo photo--courthouse" style="left:0;top:153px;width:381px;height:268px" role="img" aria-label="Photo of a bronze Lady Justice statue in front of a columned courthouse"></div>
    <div class="band band--navy cover-sub" style="top:421px;height:75px;padding-top:8px">
      <div class="cover-sub__title">Comprehensive Offender Programs</div>
      <div class="cover-sub__stages caps">Pre-Trial &nbsp;-&nbsp; Diversion &nbsp;-&nbsp; Deferred Prosecution<br>Jail Alternative &nbsp;-&nbsp; Probation</div>
    </div>
  </div>
</section>

<section class="spread spread--inner" aria-label="Inner spread">
  <div class="panel panel--left">
    <div class="band band--navy intro" style="top:0;height:156px">
      <div class="cond-title intro__title">Comprehensive Offender Solution</div>
      <div class="caps intro__lead">We administer Offender Programs at every stage of<br>the criminal justice process</div>
      <svg class="stages" width="355" height="32" viewBox="0 0 355 32" aria-label="Program stages: Pre-Trial, Diversion, Deferred Prosecution, Jail Alternative, Probation">
        <ellipse cx="22" cy="16" rx="20" ry="11" fill="#555b66"/>
        <polygon points="44,6 98,6 106,16 98,26 44,26" fill="#2f7fc9"/>
        <polygon points="100,6 146,6 154,16 146,26 100,26 108,16" fill="#2f7fc9"/>
        <polygon points="148,4 198,4 206,16 198,28 148,28 156,16" fill="#2f7fc9"/>
        <ellipse cx="222" cy="16" rx="16" ry="9" fill="#6b4b2c"/>
        <polygon points="238,6 282,6 290,16 282,26 238,26 246,16" fill="#2f7fc9"/>
        <polygon points="284,6 326,6 334,16 326,26 284,26 292,16" fill="#2f7fc9"/>
        <circle cx="345" cy="16" r="10" fill="#b89a4a"/>
        <g fill="#fff" font-family="Open Sans, Arial, sans-serif" font-size="6.5" font-weight="600">
          <text x="58" y="18.5">Pre-Trial</text>
          <text x="114" y="18.5">Diversion</text>
          <text x="164" y="14">Deferred</text>
          <text x="160" y="22">Prosecution</text>
          <text x="258" y="14">Jail</text>
          <text x="250" y="22">Alternative</text>
          <text x="296" y="18.5">Probation</text>
        </g>
      </svg>
    </div>
    <div class="band band--silver pitch" style="top:156px;height:155px">
      <div class="pitch__head">flexible solution for<span>your jurisdiction’s needs</span></div>
      <div class="pitch__body">Not a one size fits all solution:<br>each program developed and administered to your<br>specification</div>
    </div>
    <div class="band band--slate strip strip--phone" style="top:311px">1-800-555-0142</div>
  </div>

  <div class="panel panel--right">
    <div class="photo photo--meeting" style="left:18px;top:12px;width:345px;height:137px" role="img" aria-label="Photo of a couple meeting with an advisor at a desk"></div>
    <div class="band band--slate custom" style="top:149px;height:35px;left:18px;width:345px">
      <div class="caps custom__title">Custom Solution</div>
      <div class="custom__note">All offender programs are customized to meet the unique needs of your jurisdiction</div>
    </div>
    <div class="band band--silver" style="top:184px;height:127px"></div>
    <div class="menus">
      <div class="menu menu--full">
        <div class="caps menu__title">Full menu of Conditions</div>
        <div class="menu__cols">
          <ul>
            <li>Case Management</li><li>Offender Education</li><li>Fine and Fee Recovery</li>
            <li>Interactive Journaling</li><li>Alcohol monitoring</li><li>Community Resource Referrals</li>
            <li>Curfew monitoring</li><li>Offender Communication</li><li>Reporting</li>
          </ul>
          <ul>
            <li>Face to face meetings</li><li>Group Counselling</li><li>Victim Restitution Recovery</li>
            <li>Drug testing</li><li>Community Service</li><li>GPS monitoring</li>
            <li>House detention</li><li>Preparation of court paperwork</li>
          </ul>
        </div>
      </div>
      <div class="menu menu--admin">
        <div class="caps menu__title">Comprehensive<br>Administrative Services</div>
        <ul>
          <li>Eligible case screening</li><li>Case referral</li><li>Data entry</li>
          <li>Electronic case files</li><li>Offender communication</li><li>Reporting</li>
        </ul>
      </div>
    </div>
    <div class="band band--slate strip strip--web" style="top:311px">www.meridianjustice.org</div>
  </div>

  <div class="features band--navy">
    <article class="feature">
      <h3 class="caps feature__title">Experienced<br>Professionals</h3>
      <p>Our case management and operations team has over 25+ years of experience developing and administering programs for prosecutors, courts and probation. Each program has unique requirements for the participants based on the goals of each jurisdiction.</p>
    </article>
    <article class="feature">
      <h3 class="caps feature__title">Control /<br>Transparency</h3>
      <p>Your office establishes the parameters and offender requirements for each program and always maintains the control to change program guidelines at any time.</p>
      <p>We provide you and your designated staff with 24/7 online access to all case files that contain a record of every action taken on each case.</p>
    </article>
    <article class="feature">
      <h3 class="caps feature__title">Save Resources /<br>Reduce case loads</h3>
      <p>We provide the resources to reduce your staff's workload and facilitate a quick resolution to cases. Our staff handles all program administrative responsibilities from case referral to resolution and reporting.</p>
    </article>
    <article class="feature">
      <h3 class="caps feature__title">Technology /<br>Equipment</h3>
      <p>We utilize technology to automate processes that in turn allows our staff to focus on interactions with the offenders.</p>
      <p>When electronic monitoring is required, we use only the latest and most current equipment models to ensure the accurate offender accountability and public safety.</p>
    </article>
  </div>
</section>

</body>
</html>
```